Business Card Design

We just need these details on one side of card and logo on the other.

Industry/Entity Type

Business

Contact Information for Business Card

Colette Marsh | Artist
87 Tillbrook Lane
Dunmore Heights Vic 3172
# 0418 207 913 | 03 9386 2417
colette@colettemarsh-example.com
colettesstudio-example.com.au

```html
<!DOCTYPE html>
<html lang="en">
<head>
<meta charset="utf-8">
<title>Colette's Studio – Business Card</title>
<link rel="stylesheet" href="https://fonts.googleapis.com/css2?family=Alice&family=Raleway:wght@400&display=swap">
<style>
  :root {
    --backdrop-light: #e6e6e7;
    --backdrop-dark: #8f8f93;
    --card-top: #2b2b2b;
    --card-bottom: #1b1b1b;
    --text-grey: #8e8e8e;
    --text-light: #c9c9c9;
    --text-white: #f2f2f2;
    --rule: #e8e8e8;
    --ghost: rgba(255, 255, 255, 0.07);
  }
  * { margin: 0; padding: 0; box-sizing: border-box; }
  html, body { width: 1200px; height: 1000px; overflow: hidden; }
  body {
    position: relative;
    background: radial-gradient(ellipse at 50% 50%, var(--backdrop-light) 0%, var(--backdrop-dark) 80%);
    font-family: "Alice", serif;
  }
  .card {
    position: absolute;
    width: 666px;
    height: 410px;
    left: 265px;
    background: linear-gradient(180deg, var(--card-top), var(--card-bottom));
    box-shadow: 0 2px 8px rgba(0,0,0,0.35);
    overflow: hidden;
  }
  .card--front { top: 61px; }
  .card--back { top: 501px; }
  .card__texture { position: absolute; inset: 0; }
  .abs { position: absolute; white-space: nowrap; }
  .centered { transform: translateX(-50%); text-align: center; }

  .brand-name {
    left: 333px; top: 128px;
    font-size: 70px; color: var(--text-grey);
  }
  .brand-tagline {
    left: 333px; top: 220px;
    font-family: "Raleway", sans-serif;
    font-size: 16px; letter-spacing: 2px; color: var(--text-grey);
  }
  .brand-tagline .sep { display: inline-block; width: 5px; height: 5px; border-radius: 50%; background: var(--text-grey); vertical-align: middle; margin: 0 10px; }

  .website-rule { left: 190px; top: 336px; width: 286px; height: 2px; background: var(--rule); }
  .website-icon { left: 318px; top: 310px; }
  .website { left: 333px; top: 338px; font-size: 18px; color: var(--text-light); letter-spacing: 0.5px; }

  .ghost-brand { left: 350px; top: 140px; font-size: 70px; color: var(--ghost); }
  .ghost-tagline { left: 350px; top: 232px; font-family: "Raleway", sans-serif; font-size: 16px; letter-spacing: 2px; color: var(--ghost); }

  .email { left: 336px; top: 52px; font-size: 22px; color: var(--text-light); }
  .email-rule { left: 170px; top: 87px; width: 330px; height: 2px; background: var(--rule); }
  .email-icon { left: 316px; top: 90px; }

  .person { left: 150px; top: 138px; font-size: 40px; color: var(--text-grey); }
  .person .divider { display: inline-block; width: 2px; height: 38px; background: var(--text-white); vertical-align: -6px; margin: 0 8px 0 10px; }
  .person .role { font-size: 26px; color: var(--text-white); }

  .address { left: 333px; top: 215px; font-size: 25px; line-height: 28px; color: var(--text-light); letter-spacing: 0.5px; }

  .phone-rule { top: 327px; width: 198px; height: 2px; background: var(--rule); }
  .phone-rule--mobile { left: 54px; }
  .phone-rule--office { left: 425px; }
  .phone-icon { top: 294px; }
  .phone-icon--mobile { left: 135px; }
  .phone-icon--office { left: 506px; }
  .phone { top: 332px; font-size: 25px; color: var(--text-grey); }
  .phone--mobile { left: 153px; }
  .phone--office { left: 524px; }
</style>
</head>
<body>

<section class="card card--front">
  <div class="card__texture" role="img" aria-label="Dark charcoal wood-grain texture"></div>
  <div class="abs centered brand-name">Colette's Studio</div>
  <div class="abs centered brand-tagline">STUDIO<span class="sep"></span>CAFE<span class="sep"></span>GALLERY</div>
  <svg class="abs website-icon" width="30" height="26" viewBox="0 0 30 26" aria-hidden="true">
    <g fill="none" stroke="#eee" stroke-width="1.5">
      <circle cx="11" cy="11" r="9"/>
      <ellipse cx="11" cy="11" rx="4" ry="9"/>
      <line x1="2" y1="11" x2="20" y2="11"/>
      <line x1="4" y1="6" x2="18" y2="6"/>
      <line x1="4" y1="16" x2="18" y2="16"/>
      <line x1="18" y1="18" x2="28" y2="25" stroke-width="3"/>
    </g>
  </svg>
  <div class="abs website-rule"></div>
  <div class="abs centered website">colettesstudio-example.com.au</div>
</section>

<section class="card card--back">
  <div class="card__texture" role="img" aria-label="Dark charcoal wood-grain texture"></div>
  <div class="abs centered ghost-brand">Colette's Studio</div>
  <div class="abs centered ghost-tagline">STUDIO · CAFE · GALLERY</div>

  <div class="abs centered email">colette@colettemarsh-example.com</div>
  <div class="abs email-rule"></div>
  <svg class="abs email-icon" width="38" height="18" viewBox="0 0 38 18" aria-hidden="true">
    <g fill="none" stroke="#eee" stroke-width="1.3">
      <rect x="1" y="1" width="36" height="16"/>
      <polyline points="1,1 19,11 37,1"/>
    </g>
  </svg>

  <div class="abs person">Colette Marsh<span class="divider"></span><span class="role">Artist</span></div>
  <div class="abs centered address">87 Tillbrook Lane<br>Dunmore Heights 3172</div>

  <svg class="abs phone-icon phone-icon--mobile" width="36" height="32" viewBox="0 0 36 32" aria-hidden="true">
    <g transform="rotate(-35 18 16)" fill="none" stroke="#eee" stroke-width="1.6">
      <rect x="11" y="2" width="14" height="28" rx="3"/>
      <line x1="15" y1="6" x2="21" y2="6"/>
      <circle cx="18" cy="26" r="1.3"/>
    </g>
  </svg>
  <div class="abs phone-rule phone-rule--mobile"></div>
  <div class="abs centered phone phone--mobile">0418 207 913</div>

  <svg class="abs phone-icon phone-icon--office" width="36" height="32" viewBox="0 0 36 32" aria-hidden="true">
    <g transform="rotate(-35 18 16)" fill="none" stroke="#eee" stroke-width="1.6">
      <rect x="11" y="2" width="14" height="28" rx="3"/>
      <line x1="15" y1="6" x2="21" y2="6"/>
      <circle cx="18" cy="26" r="1.3"/>
    </g>
  </svg>
  <div class="abs phone-rule phone-rule--office"></div>
  <div class="abs centered phone phone--office">03 9386 2417</div>
</section>

</body>
</html>
```